A parent Company needs a website as a leading diversified business in industrial Conglomerates in Af

Tesku Group is a private (Holding) limited liability company incorporated under the Companies Code, 1963 (Act 179) in November, 2013 to following the speedy growth in numbers of its current subsidiaries which has been founded several years ago with an emerging force to become one of the largest and a leading diversified business in industrial Conglomerates in Africa.
The Group which is 100% wholly owned indigenous Ghanaian Company focuses on provision of local, value-added products and services that meet the needs of the African population. The Group is headquartered in Accra, Ghana with interests across a range of sectors in Africa.
We are currently into Food & Beverage, Real Estate Development, Transportation, Health Care, Consumer Products Distribution, Agro Processing, Manufacturing, ICT, Exports & Import, and still counting.
In the next 3 years, we shall announce our ambitions to enter Ghana's largest Oil and Gas industry, playing a strategic role in the petroleum sector with strategic alliances, and help build Ghana's biggest and most important Energy sector in the country.
Inspired by billionaires Ned Harlow, Colin Ashdown, and Efemi Okorusa, Tesku Group (Tesku Foundation) is committed to making a name for itself on the philanthropic circuit and has given away privately and still given to the cause to the needy in the society and some specific social causes in Ghana.
The company is managed by a 5 member board and a 2 member advisory experts who are non-board members.
The company has a vision, mission and it is guided by its core values.
We would like to see a designs that is very professional and looks corporate and can attract investors and partners. It must communicate financial safety and growth and must reflect our logo colors.

```html
<!DOCTYPE html>
<html lang="en">
<head>
<meta charset="utf-8">
<title>Tesku Group</title>
<link rel="stylesheet" href="https://fonts.googleapis.com/css2?family=Open+Sans:wght@300;400;600&display=swap">
<style>
  :root {
    --red: #e4262f;
    --blue: #0a63b3;
    --navy: #1d2a5c;
    --grey: #7a7a7a;
    --text: #5a5a5a;
    --dark: #333333;
    --topbar: #f7f7f7;
    --line: #e6e6e6;
    --footer: #dedede;
    --white: #ffffff;
  }
  * { margin: 0; padding: 0; box-sizing: border-box; }
  html, body { width: 1200px; height: 789px; overflow: hidden; background: var(--white); }
  body { font-family: "Open Sans", Arial, sans-serif; color: var(--text); position: relative; }

  .topbar { position: absolute; left: 0; top: 0; width: 1200px; height: 24px; background: var(--topbar); border-bottom: 1px solid var(--line); }
  .topbar-list { position: absolute; right: 119px; top: 4px; display: flex; align-items: center; font-size: 12px; font-weight: 300; color: #777; list-style: none; }
  .topbar-list li { display: flex; align-items: center; gap: 6px; }
  .topbar-list .sep { width: 1px; height: 14px; background: #aaa; margin: 0 16px; }
  .flag { width: 18px; height: 13px; display: block; }

  .site-header { position: absolute; left: 0; top: 24px; width: 1200px; height: 161px; border-bottom: 1px solid var(--line); }
  .brand { position: absolute; left: 150px; top: 58px; display: flex; align-items: center; gap: 8px; font-size: 16px; font-weight: 400; color: var(--dark); }
  .brand-dot { width: 12px; height: 12px; border-radius: 50%; background: var(--blue); }
  .main-nav { position: absolute; left: 519px; top: 56px; display: flex; list-style: none; font-size: 14px; font-weight: 400; color: var(--dark); }
  .main-nav li { height: 29px; line-height: 29px; margin-right: 25px; }
  .main-nav li:last-child { margin-right: 0; }
  .main-nav .active { background: var(--red); color: var(--white); padding: 0 15px; margin-right: 27px; }

  .hero { position: absolute; left: 121px; top: 157px; width: 959px; height: 326px; overflow: hidden; }
  .hero-photo { position: absolute; inset: 0; background:
      linear-gradient(90deg, #f2f2f2 0%, #eeeeee 30%, rgba(238,238,238,0) 50%),
      linear-gradient(180deg, #6f9fd0 0%, #c4d6e6 45%, #7d8690 62%, #4b4f55 100%); }
  .hero-truck { position: absolute; left: 565px; top: 0; width: 394px; height: 326px; background: linear-gradient(180deg, #c9c4b6 0%, #a9a497 60%, #2b2c2e 80%, #1c1c1d 100%); }
  .hero-title { position: absolute; left: 29px; top: 78px; font-size: 30px; font-weight: 400; line-height: 40px; color: var(--navy); }
  .hero-title em { font-style: normal; color: var(--red); }

  .sectors { position: absolute; left: 120px; top: 536px; display: flex; gap: 35px; list-style: none; }
  .sector { width: 297px; border-top: 5px solid; padding-top: 12px; }
  .sector-transport { border-color: var(--blue); }
  .sector-health { border-color: var(--red); }
  .sector-manufacturing { border-color: var(--grey); }
  .sector-title { display: flex; align-items: center; gap: 9px; font-size: 20px; font-weight: 400; line-height: 26px; }
  .sector-transport .sector-title { color: var(--blue); }
  .sector-health .sector-title { color: var(--red); }
  .sector-manufacturing .sector-title { color: #555; }
  .sector-title svg { width: 19px; height: 19px; }
  .sector p { margin-top: 7px; font-size: 13px; line-height: 19px; font-weight: 400; }
  .read-more { display: inline-block; margin-top: 18px; font-size: 12px; color: var(--dark); text-decoration: none; border-bottom: 1px solid var(--dark); line-height: 14px; }

  .site-footer { position: absolute; left: 0; top: 729px; width: 1200px; height: 44px; background: var(--footer); font-size: 11px; color: var(--dark); }
  .footer-links { position: absolute; left: 139px; top: 15px; display: flex; list-style: none; }
  .footer-links li + li::before { content: "|"; margin: 0 10px; }
  .copyright { position: absolute; right: 132px; top: 15px; }
</style>
</head>
<body>
  <div class="topbar">
    <ul class="topbar-list">
      <li><svg width="14" height="10" viewBox="0 0 14 10"><rect width="14" height="10" fill="#e4262f"/><path d="M0 0 7 6 14 0" stroke="#fff" fill="none"/></svg>info@tesku.com</li>
      <li class="sep"></li>
      <li><svg width="12" height="12" viewBox="0 0 12 12"><path d="M2 1 4 1 5 4 3.5 5a6 6 0 0 0 3.5 3.5L8 7l3 1v2a1 1 0 0 1-1 1A9 9 0 0 1 1 2a1 1 0 0 1 1-1z" fill="#e4262f"/></svg>+233 (0) 2 418 907</li>
      <li class="sep"></li>
      <li><svg width="11" height="11" viewBox="0 0 11 11"><path d="M0 0h11v8H4L1 11V8H0z" fill="#e4262f"/></svg>Language
        <svg class="flag" viewBox="0 0 18 13" aria-label="English"><rect width="18" height="13" fill="#c9303a"/><rect y="2" width="18" height="2" fill="#fff"/><rect y="6" width="18" height="2" fill="#fff"/><rect y="10" width="18" height="1.5" fill="#fff"/><rect width="8" height="7" fill="#2d4a8c"/></svg>
        <svg class="flag" viewBox="0 0 18 13" aria-label="Français"><rect width="6" height="13" fill="#2d4a8c"/><rect x="6" width="6" height="13" fill="#fff"/><rect x="12" width="6" height="13" fill="#d6303a"/></svg>
      </li>
    </ul>
  </div>

  <header class="site-header">
    <div class="brand"><span class="brand-dot"></span>Tesku Group</div>
    <ul class="main-nav">
      <li class="active">Home</li>
      <li>About Us</li>
      <li>Distribution</li>
      <li>Marketing</li>
      <li>Transportation</li>
      <li>Contact Us</li>
    </ul>
  </header>

  <section class="hero">
    <div class="hero-photo" role="img" aria-label="Photo of a cargo truck driving on a highway under a blue cloudy sky"></div>
    <div class="hero-truck" role="img" aria-label="Side of a white truck trailer"></div>
    <h1 class="hero-title">Playing a strategic role<br>in the petroleum sector<br>with strategic alliances<br>in <em>Africa</em></h1>
  </section>

  <ul class="sectors">
    <li class="sector sector-transport">
      <h2 class="sector-title"><svg viewBox="0 0 20 20"><path d="M10 1 19 18H1z" fill="#0a63b3"/><rect x="9" y="7" width="2" height="6" fill="#fff"/><rect x="9" y="14" width="2" height="2" fill="#fff"/></svg>Transportation</h2>
      <p>Le Lorem Ipsum est simplement du faux texte employé dans la composition et la mise en page avant impression. Le Lorem Ipsum est le faux texte standard de l'imprimerie.</p>
      <a class="read-more" href="#">Read More</a>
    </li>
    <li class="sector sector-health">
      <h2 class="sector-title"><svg viewBox="0 0 20 20"><path d="M14 2l4 4M16 4l-3 3M12 5l3 3-8 8-3-1-1-3z M3 14l-2 5 5-2" stroke="#e4262f" stroke-width="2" fill="none"/></svg>Healthcare</h2>
      <p>Le Lorem Ipsum est simplement du faux texte employé dans la composition et la mise en page avant impression. Le Lorem Ipsum est le faux texte standard de l'imprimerie.</p>
      <a class="read-more" href="#">Read More</a>
    </li>
    <li class="sector sector-manufacturing">
      <h2 class="sector-title"><svg viewBox="0 0 20 20"><circle cx="5" cy="5" r="4" fill="#666"/><circle cx="15" cy="5" r="4" fill="#666"/><circle cx="10" cy="14" r="4" fill="#999"/></svg>Manafacturing</h2>
      <p>Le Lorem Ipsum est simplement du faux texte employé dans la composition et la mise en page avant impression. Le Lorem Ipsum est le faux texte standard de l'imprimerie.</p>
      <a class="read-more" href="#">Read More</a>
    </li>
  </ul>

  <footer class="site-footer">
    <ul class="footer-links">
      <li>Home</li>
      <li>Sitemap</li>
      <li>Term &amp; Condintions</li>
    </ul>
    <div class="copyright">© Copyright teskugroup 2014</div>
  </footer>
</body>
</html>
```